businesscard, flyer and membercard

--------------------------------------------------------------------------------------------------
design flyer :
- delivering format (jpg, pdf and original psd)
- there is a example how the flyers should look like
the text and logo should be the same as the exemple flyer, the creativity is yours.
- the design should have a back and front side.
File format : 15,0 cm x 21,2 cm
design membercard :
- there is example how the member-card should look like
the text and logo should be the same as the exemple membercard, the creativity is yours.
- the front side contains text and open space where for writing :
Naam ......
Dansstijlen ......
- the front side contains 12 circels horizontal at the line name at the end of the line "Salsa".
- the front side contains 12 circels horizontal at the line name at the end of the line "Bachata".
- the front side contains 12 circels horizontal at the line name at the end of the line "Kizomba".
- each horizontal line with circels contains a different kind of color/design.
- file format: 7,6 cm x 10,7 cm
Business card :
- there is example how the businesscard should look like
the text and logo should be the same as the exemple buisinesscard, the creativity is yours.
- the design should have a back a front side
File format : 8,7 cm x 5,7 cm

Target Market(s)

Dancing :Salsa, Bachata and Kizomba

Colors

Designer to choose colors to be used in the design.

Requirements
Must have
• same text as seen on the examples.
Nice to have
• see the examples as attachments
Should not have
• - REMOVE TEXT "KOV" from the design
• - REMOVE TEXT "Gratis Parkeren"

```html
<!DOCTYPE html>
<html lang="nl">
<head>
<meta charset="utf-8">
<title>Velora Dance Studio – Flyers</title>
<link href="https://fonts.googleapis.com/css2?family=Roboto+Condensed:ital,wght@0,400;0,700;1,700&family=Roboto:ital,wght@0,400;0,900;1,400&family=Playball&family=Oswald:wght@500&display=swap" rel="stylesheet">
<style>
:root{
  --page:#2b2522;
  --ink:#0e0b0c;
  --teal:#1a7f9c;
  --teal-deep:#0b3a4d;
  --gold:#f2c335;
  --yellow:#f5e25a;
  --white:#ffffff;
  --red:#e8382c;
}
*{margin:0;padding:0;box-sizing:border-box}
html,body{width:1200px;height:1200px;overflow:hidden;background:var(--page)}
.stage{position:absolute;left:0;top:0;width:1400px;height:1400px;transform:scale(.857143);transform-origin:0 0}
.flyer{position:absolute;top:266px;width:615px;height:870px;overflow:hidden;color:var(--white);
  background:
    radial-gradient(ellipse 42% 11% at 76% 10%,rgba(255,255,255,.92) 0%,rgba(220,235,250,.7) 55%,transparent 100%),
    radial-gradient(ellipse 30% 18% at 50% 0%,rgba(255,250,235,.8),transparent 75%),
    radial-gradient(ellipse 18% 10% at 0% 0%,rgba(255,190,90,.8),transparent 80%),
    radial-gradient(ellipse 18% 10% at 100% 0%,rgba(255,190,90,.8),transparent 80%),
    radial-gradient(ellipse 70% 50% at 55% 45%,var(--teal) 0%,var(--teal-deep) 60%,transparent 100%),
    linear-gradient(180deg,#3a5f9a 0%,#0d2f40 45%,#14121a 66%,var(--ink) 75%);
  box-shadow:0 6px 18px rgba(0,0,0,.6)}
.flyer--front{left:68px}
.flyer--back{left:715px}
.abs{position:absolute}
.brand{left:70px;top:62px;font-family:'Roboto',sans-serif;font-weight:400;font-size:34px;letter-spacing:6px;color:var(--white);line-height:1}
.studio{left:285px;top:60px;width:310px;text-align:center;font-family:'Roboto',sans-serif;font-weight:900;font-size:37px;line-height:1;color:var(--ink);letter-spacing:1px}
.tagline{left:285px;top:99px;width:310px;text-align:center;font-family:'Roboto',sans-serif;font-style:italic;font-size:10.5px;line-height:1;color:#222}
.dancers{left:150px;top:160px;width:410px;height:430px;border-radius:8px;
  background:radial-gradient(ellipse 40% 50% at 50% 55%,rgba(220,60,45,.55),rgba(20,20,25,.35) 70%,transparent 100%)}
.styles{font-family:'Playball',cursive;font-size:50px;line-height:1}
.styles--yellow{color:var(--yellow)}
.headline{left:0;top:612px;width:615px;text-align:center;font-family:'Oswald',sans-serif;font-weight:500;font-size:50px;line-height:1;color:var(--gold)}
.dates{left:0;top:674px;width:615px;text-align:center;font-family:'Roboto Condensed',sans-serif;font-style:italic;font-weight:700;font-size:40px;line-height:1}
.perk{font-family:'Roboto Condensed',sans-serif;font-size:15px;line-height:1.2;color:var(--yellow)}
.perk::before{content:"";position:absolute;left:-20px;top:5px;width:9px;height:9px;border-radius:50%;background:var(--white)}
.footer{top:816px;font-family:'Roboto Condensed',sans-serif;font-size:14px;line-height:1.2;padding-bottom:6px;border-bottom:1px solid rgba(255,255,255,.35)}
.footer--sans{font-family:'Roboto',sans-serif;font-size:13px}
.footer .lbl{color:var(--yellow)}
.badge{top:436px;width:96px;height:108px}
.badge span{position:absolute;inset:0;display:flex;align-items:center;justify-content:center;text-align:center;font-family:'Roboto Condensed',sans-serif;font-weight:700;font-size:16px;line-height:1.3}
.section{top:572px;font-family:'Oswald',sans-serif;font-weight:500;font-size:36px;line-height:1.2}
.section--title{left:42px;color:#e6e6e6}
.section--club{right:45px;color:var(--gold)}
.day{top:648px;width:130px;text-align:center}
.day b{display:inline-block;padding:4px 14px;border-radius:14px;background:linear-gradient(#fff,#bdbdbd);color:#222;font-family:'Roboto Condensed',sans-serif;font-weight:700;font-size:15px}
.day ul{list-style:none;margin-top:18px;font-family:'Roboto',sans-serif;font-size:15px;color:var(--yellow);line-height:29px}
.divider{top:640px;width:2px;height:135px;background:linear-gradient(transparent,rgba(255,255,255,.7),transparent)}
</style>
</head>
<body>
<main class="stage">

  <section class="flyer flyer--front">
    <div class="abs brand">VELORA</div>
    <div class="abs studio">DANCE STUDIO</div>
    <div class="abs tagline">LET THE MUSIC BRING US TOGETHER</div>
    <div class="abs dancers" role="img" aria-label="Photo of a dancing couple, man in black and woman in a red ruffled dress, in a dramatic dip pose"></div>
    <div class="abs styles styles--yellow" style="left:30px;top:228px">Salsa</div>
    <div class="abs styles" style="left:30px;top:292px">Bachata</div>
    <div class="abs styles styles--yellow" style="left:30px;top:350px">Kizomba</div>

    <div class="abs headline">GRATIS PROEFLESSEN</div>
    <div class="abs dates">26 t/m 28 Sept</div>
    <div class="abs perk" style="left:125px;top:738px">EERSTE LES GRATIS</div>
    <div class="abs perk" style="left:125px;top:764px">STUDENTE KORTING</div>
    <div class="abs perk" style="left:398px;top:737px">ELK NIVEAU</div>
    <div class="abs perk" style="left:398px;top:763px">ALLE LEEFTIJDEN</div>

    <div class="abs footer" style="left:76px">Danslaan 12, 2511 AB Den Haag</div>
    <div class="abs footer" style="left:267px"><span class="lbl">Socials</span> : Veloradance</div>
    <div class="abs footer" style="left:438px"><span class="lbl">Tel</span> : 0612345678</div>
  </section>

  <section class="flyer flyer--back">
    <div class="abs brand">VELORA</div>
    <div class="abs studio">DANCE STUDIO</div>
    <div class="abs tagline">LET THE MUSIC BRING US TOGETHER</div>
    <div class="abs dancers" style="left:160px;top:120px;height:420px" role="img" aria-label="Photo of a dancing couple, man in black and woman in a red ruffled dress, in a dramatic dip pose"></div>
    <div class="abs styles styles--yellow" style="left:35px;top:197px">Salsa</div>
    <div class="abs styles" style="left:35px;top:262px">Bachata</div>
    <div class="abs styles styles--yellow" style="left:35px;top:318px">Kizomba</div>

    <div class="abs badge" style="left:34px">
      <svg width="96" height="108" viewBox="0 0 96 108"><polygon points="48,3 93,29 93,79 48,105 3,79 3,29" fill="#111" stroke="#f2c335" stroke-width="4"/></svg>
      <span>Altijd<br>Eerste Les<br>Gratis</span>
    </div>

    <div class="abs section section--title">LES ROOSTER</div>
    <div class="abs section section--club">CLUB ORIONIS</div>

    <div class="abs day" style="left:50px"><b>DINSDAG</b>
      <ul><li>19:00 Salsa 1</li><li>20:00 Salsa 3</li><li>21:00 Bachata 3</li></ul></div>
    <div class="abs divider" style="left:201px"></div>
    <div class="abs day" style="left:239px"><b>WOENSDAG</b>
      <ul><li>19:00 Kizomba 2</li><li>20:00 Kizomba 1</li><li>21:00 Kizomba 3</li></ul></div>
    <div class="abs divider" style="left:399px"></div>
    <div class="abs day" style="left:436px"><b>DONDERDAG</b>
      <ul><li>19:00 Salsa 2</li><li>20:00 Bachata 1</li><li>21:00 Bachata 2</li></ul></div>

    <div class="abs footer footer--sans" style="left:35px">Danslaan 12, 2511 AB Den Haag</div>
    <div class="abs footer footer--sans" style="left:234px"><span class="lbl">Socials</span> : Veloradance</div>
    <div class="abs footer footer--sans" style="left:458px"><span class="lbl">Tel</span> : 0612345678</div>
  </section>

</main>
</body>
</html>
```